Trampoline Website Redesign Photoshop

I need a new design for me Trampolines online store using more real life images

http://www.bouncyardco.com.au

Looking for an image rich-non oscommerce look

Some cool examples I like:

http://www.pardonwool.com/
http://glumbarrow.com/
http://www.windyquaytrader.co.uk/
http://wendafrost.com/

But obviously don't want a copy of any of the above solutions....

Target Market(s)

parents of children, typically 25-45

Number of Pages Required

2 pages

Requirements
Must have
• -must use real life images provided

• -retain colour scheme and logos

• -must mention all our products

• -must have our two product types: Spring Trampolines (8, 10, 12,14,15,16ft) and Springless Trampolines (8, 10, 12,14,15,16ft) with prices on home page

• Must use high conversion techniques for home and product pages

• Must use information provided on our website

• Video currently embedded in sidebar must be there somewhere

• All content will remain the same

• Please use images in provided file and any images on the website http://www.bouncyardco.com.au
Should not have
• no stock images

```html
<!DOCTYPE html>
<html lang="en">
<head>
<meta charset="utf-8">
<title>Bounce Yard Co – Trampolines Online</title>
<link href="https://fonts.googleapis.com/css2?family=Nunito:ital,wght@0,700;0,800;1,700;1,800&family=Arimo:ital,wght@0,400;0,700;1,400&display=swap" rel="stylesheet">
<style>
:root{
  --grey-text:#7a7a7a;
  --grey-line:#c8c8c8;
  --blue:#33a7d3;
  --bubble:#6aa9dc;
  --lime:#b4d43a;
  --orange:#f0ae25;
  --teal:#67beaf;
  --panel:#ececec;
  --thumb-bar:#3a72c4;
  --badge:#f26b22;
  --white:#fff;
}
*{box-sizing:border-box;margin:0;padding:0}
html,body{width:1129px;height:1200px;overflow:hidden;background:var(--white)}
body{position:relative;font-family:"Arimo",Arial,sans-serif;color:var(--grey-text)}
.abs{position:absolute}
.heading{font-family:"Nunito",Arial,sans-serif}

.brand-mark{left:161px;top:29px;width:98px;height:98px;border-radius:50%;background:radial-gradient(circle at 45% 40%,#8fd8f5,#2a9fd3 70%);border:4px solid #cfd7db}
.brand-name{left:277px;top:55px;font-size:42px;font-weight:800;color:#8a8a8a;letter-spacing:.5px}
.tagline{right:157px;top:36px;text-align:right;font-style:italic}
.tagline .lead{font-size:17px;color:#777}
.tagline .call{font-size:12px;color:#777}
.tagline .tel{font-size:13px;color:#777}
.tagline .tel b{font-size:20px;font-weight:700;color:#666}

.nav a{position:absolute;top:118px;display:block;text-decoration:none;font-family:"Nunito",sans-serif;font-style:italic;font-weight:700;font-size:16px;color:#8c8c8c;text-align:center;height:25px;border-bottom:5px solid var(--grey-line)}
.nav a.active{border-color:var(--blue)}

.hero-photo{left:146px;top:147px;width:515px;height:277px;background:linear-gradient(180deg,#b9c9b0 0%,#93ab7e 35%,#5a7a45 55%,#2f4f3c 80%,#3a5a44 100%)}
.hero-info{left:661px;top:147px;width:327px;height:277px;background:var(--blue);border-radius:0 5px 5px 0;color:var(--white);font-size:12px;line-height:21px;padding:22px 18px}
.hero-info p+p{margin-top:21px}
.socials{left:680px;top:389px;display:flex;gap:4px;align-items:center}
.socials span{font-size:9px;font-weight:700;color:var(--white);background:#2b86b5;padding:7px 3px;border-radius:3px;line-height:11px}
.order-now{left:821px;top:386px;width:149px;height:38px;background:var(--lime);color:var(--white);text-decoration:none;font-family:"Nunito",sans-serif;font-weight:800;font-size:16px;padding:6px 12px 6px 11px;display:flex;justify-content:space-between;align-items:center}

.tab{top:430px;height:61px;border-radius:3px;color:var(--white);font-family:"Nunito",sans-serif;font-style:italic;font-weight:800;font-size:20px;padding:16px 0 0 24px;white-space:nowrap}
.tab.spring{left:150px;width:239px;background:var(--orange)}
.tab.springfree{left:395px;width:261px;background:var(--teal);padding-left:11px}

.guarantee{left:662px;top:427px;width:326px;height:124px;background:var(--panel);border-radius:0 0 4px 4px;padding:9px 16px;font-size:12px;line-height:18px;color:#777}
.guarantee h3{font-family:"Nunito",sans-serif;font-style:italic;font-size:15px;color:#777;margin-bottom:0}

.prices-title{left:170px;top:512px;font-size:22px;font-weight:800;color:#7d7d7d}
.price-list{left:170px;top:552px;list-style:none;font-size:13px;color:#777}
.price-list li{height:28px}
.pitch{left:352px;top:551px;width:290px;font-size:12px;font-style:italic;line-height:18px;color:#777}
.pitch p{margin-bottom:18px}
.pitch .cta{color:#33a7d3;font-weight:700;font-size:13px;margin-top:6px}

.section-label{left:157px;font-size:13px;color:#777}
.thumb{width:149px;height:115px}
.thumb .bar{position:absolute;right:0;bottom:0;background:var(--thumb-bar);color:var(--white);font-size:9px;font-weight:700;padding:3px 4px}
.t-spring{background:linear-gradient(180deg,#a9bd8c,#8aa46c 40%,#5b6d64 65%,#6f8d53)}
.t-free{background:linear-gradient(180deg,#a6b8a0,#6d8d60 45%,#2e4b3a 75%,#5e7d55)}

.body-copy{left:157px;top:1004px;width:484px;font-size:12px;font-style:italic;line-height:18px;color:#777}
.body-copy p+p{margin-top:18px}

.product-shot{left:664px;top:553px;width:152px;height:158px;background:linear-gradient(180deg,#dfe3e4,#aab3b6 60%,#4aa3d6 80%,#e6e6e6)}
.free-badge{left:724px;top:628px;width:95px;height:95px;border-radius:50%;background:var(--badge);color:var(--white);text-align:center;transform:rotate(-18deg);padding-top:22px;font-weight:700}
.free-badge small{display:block;font-size:10px;line-height:11px}
.free-badge b{font-size:30px;line-height:32px}
.ticks{left:823px;top:582px;list-style:none;font-size:12px;font-style:italic;line-height:18px;color:#777}
.ticks li{display:flex;gap:4px;align-items:flex-start}

.secure-badge{left:668px;top:736px;width:89px;height:42px;background:linear-gradient(180deg,#e0e0e0,#a8a8a8);border-radius:3px}
.secure-note{left:771px;top:736px;font-size:9px;line-height:12px;color:#555}
.cards{left:771px;top:771px;display:flex;gap:5px}
.cards span{width:42px;height:26px;border:1px solid #ccc;font-size:9px;font-weight:700;color:#555;display:flex;align-items:center;justify-content:center;background:#f7f7f7}

.reviews-title{left:678px;top:824px;font-size:15px;font-style:italic;color:#777}
.bubble{left:671px;width:301px;background:var(--bubble);color:var(--white);font-size:12px;line-height:14px;padding:7px 4px 7px 8px;border-radius:8px;letter-spacing:-.2px}
.reviewer{left:679px;font-size:12px;font-weight:700;color:#666}
.tail{width:20px;height:14px}

.cart-title{left:676px;top:1084px;font-size:13px;color:#777}
.cart-items{left:676px;top:1101px;font-size:12px;color:#777}
.cart-total{left:661px;top:1128px;width:328px;height:27px;background:var(--lime);color:var(--white);font-weight:700;font-size:13px;padding:6px 15px}

.footer{left:146px;top:1167px;width:842px;height:22px;background:#b1b1b1;border-radius:3px;color:var(--white);font-size:14px;text-align:center;line-height:22px}
</style>
</head>
<body>

<header>
  <div class="abs brand-mark"></div>
  <div class="abs brand-name heading">Bounce Yard Co</div>
  <div class="abs tagline">
    <div class="lead">Reliable. Fast.&nbsp; Easy delivery.</div>
    <div class="call">Call us now.</div>
    <div class="tel">Tel. <b>03 5550 1842</b></div>
  </div>
  <nav class="nav">
    <a class="active" href="#" style="left:544px;width:73px">Blog</a>
    <a href="#" style="left:620px;width:89px">FAQ</a>
    <a href="#" style="left:716px;width:122px">Contact</a>
    <a href="#" style="left:855px;width:133px">Shipping Info</a>
  </nav>
</header>

<section>
  <div class="abs hero-photo" role="img" aria-label="Photo of a child jumping on a green-padded trampoline in a park"></div>
  <div class="abs hero-info">
    <p>High Quality Trampolines Online<br>Make the kids happy while reliving<br>your childhood with our high quality<br>Trampoline's, available in a variety of sizes<br>to suit all backyards and people.</p>
    <p>We carry 8ft Trampolines , 10ft Trampolines ,<br>&nbsp;12ft Trampolines , 14ft Trampolines ,<br>15ft Trampolines in stock and ready to ship.</p>
  </div>
  <div class="abs socials"><span>Linkora</span><span>Chirpnet</span><span>Clipster</span></div>
  <a class="abs order-now" href="#">Order Now
    <svg width="22" height="22" viewBox="0 0 22 22"><circle cx="11" cy="11" r="10" fill="#fff"/><path d="M6 11h9M11 6.5l4.5 4.5-4.5 4.5" stroke="#9bb92a" stroke-width="2.4" fill="none"/></svg>
  </a>
</section>

<div class="abs tab spring">Spring Trampoline</div>
<div class="abs tab springfree">Spring-free Trampoline</div>

<aside class="abs guarantee">
  <h3>Our Guarantee</h3>
  We are so confident in our products; we offer a 3 year warranty on the Trampoline frame, and a 1 year war&shy;ranty on the Trampoline Mat, giving you piece of mind in our Trampolines.
</aside>

<h2 class="abs prices-title heading">Prices have DROPPED TODAY!</h2>
<ul class="abs price-list">
  <li>8ft Trampoline:&nbsp;&nbsp; $290.00</li>
  <li>10ft Trampoline: $340.00</li>
  <li>12ft Trampoline: $380.00</li>
  <li>14ft Trampoline: $420.00</li>
  <li>15ft Trampoline: $460.00</li>
</ul>
<div class="abs pitch">
  <p>Get them now while we still have stock!</p>
  <p>Bounce Yard Co is an Australian Owned, Online Trampoline Store servicing the whole of Australia. We offer fast and relaiable shipping to anywhere in Australia, and our prices are hard to beat</p>
  <p class="cta">Get them now while we still have stock!.</p>
</div>

<div class="abs section-label" style="top:707px">Some Images of Our High Quality Spring Trampolines</div>
<div class="abs thumb t-spring" style="left:157px;top:728px" role="img" aria-label="Spring trampoline mat seen from above"><span class="bar">Order Now/ More info</span></div>
<div class="abs thumb t-spring" style="left:321px;top:728px" role="img" aria-label="Spring trampoline with blue safety padding"><span class="bar">Order Now/ More info</span></div>
<div class="abs thumb t-spring" style="left:486px;top:728px" role="img" aria-label="Spring trampoline with safety net enclosure"><span class="bar">Order Now/ More info</span></div>

<div class="abs section-label" style="top:853px">Some Images of Our High Quality Spring-free Trampolines</div>
<div class="abs thumb t-free" style="left:157px;top:874px" role="img" aria-label="Spring-free trampoline with net enclosure on grass"><span class="bar">Order Now/ More info</span></div>
<div class="abs thumb t-free" style="left:321px;top:874px" role="img" aria-label="Close view of spring-free trampoline frame and netting"><span class="bar">Order Now/ More info</span></div>
<div class="abs thumb t-free" style="left:486px;top:874px" role="img" aria-label="Child jumping inside a spring-free trampoline enclosure"><span class="bar">Order Now/ More info</span></div>

<div class="abs body-copy">
  <p>So if you are looking for a great gift for your kids or just a way to encourage them to spend some more time outside then a trampoline is perfect for you. There are so few things that will make both the parents and the kids happy, so buy a trampoline today and watch your kids grow into confident, healthy and fit individuals!</p>
  <p>A trampoline is not just a great, fun, play thing for the kids; it is also a very effective form of physical activity, that they can enjoy and reap the health benefits.</p>
</div>

<div class="abs product-shot" role="img" aria-label="Trampoline with safety net enclosure on white background"></div>
<div class="abs free-badge"><small>Safety Nets<br>included</small><b>FREE</b></div>
<ul class="abs ticks">
  <li><svg width="14" height="14" viewBox="0 0 14 14"><rect x="1" y="3" width="10" height="10" fill="none" stroke="#888"/><path d="M3 8l3 3 7-9" stroke="#666" stroke-width="1.8" fill="none"/></svg>Highest Quality</li>
  <li style="padding-left:18px">Trampolines in the Market</li>
  <li><svg width="14" height="14" viewBox="0 0 14 14"><rect x="1" y="3" width="10" height="10" fill="none" stroke="#888"/><path d="M3 8l3 3 7-9" stroke="#666" stroke-width="1.8" fill="none"/></svg>Ships Next Day</li>
  <li><svg width="14" height="14" viewBox="0 0 14 14"><rect x="1" y="3" width="10" height="10" fill="none" stroke="#888"/><path d="M3 8l3 3 7-9" stroke="#666" stroke-width="1.8" fill="none"/></svg>3 Year Warranty</li>
  <li><svg width="14" height="14" viewBox="0 0 14 14"><rect x="1" y="3" width="10" height="10" fill="none" stroke="#888"/><path d="M3 8l3 3 7-9" stroke="#666" stroke-width="1.8" fill="none"/></svg>Money Back Guarantee</li>
</ul>

<div class="abs secure-badge"></div>
<div class="abs secure-note">We offer 128 bit encryption<br>on all transactions through Gatewise Secure</div>
<div class="abs cards"><span>Cardex</span><span>Paynet</span><span style="width:56px">Walletly</span></div>

<h3 class="abs reviews-title heading">What Our Customers our Saying</h3>

<div class="abs bubble" style="top:847px">"Fast delivery, easy order process and a fantastic product. I think I may love it more than my kids do!"</div>
<svg class="abs tail" style="left:755px;top:886px" viewBox="0 0 20 14"><path d="M0 0h16q-2 10 4 14Q6 12 0 0z" fill="#6aa9dc"/></svg>
<div class="abs reviewer" style="top:897px">Marcus, Kew</div>

<div class="abs bubble" style="top:922px;padding-right:2px">"Great service and fantastic product. I ordered it only 3 days before my child's birthday and it was delivered on time as promised."</div>
<svg class="abs tail" style="left:765px;top:970px" viewBox="0 0 20 14"><path d="M0 0h16q-2 10 4 14Q6 12 0 0z" fill="#6aa9dc"/></svg>
<div class="abs reviewer" style="top:981px">Toby, Sydney</div>

<div class="abs bubble" style="top:1003px;height:41px">"Seamless process, great Customer Support and fantastic prices."</div>
<svg class="abs tail" style="left:780px;top:1043px" viewBox="0 0 20 14"><path d="M0 0h16q-2 10 4 14Q6 12 0 0z" fill="#6aa9dc"/></svg>
<div class="abs reviewer" style="top:1051px">Leon, Wodonga</div>

<div class="abs cart-title">Cart Info</div>
<div class="abs cart-items">Items/cost:</div>
<div class="abs cart-total">Total cost:</div>

<footer class="abs footer">Copyright © 2009 Bounce Yard Co.All rights reserved</footer>

</body>
</html>
```